Trade Show Booth for SaaS Company

Brightpost Relay is a startup company that will be exhibiting its software as a service product at a trade show in the near future. We are looking for something that really pops and is appealing to the eye. Attached is the branding guidelines along with the color palette.
Also attached is a previous design we have used and you can take to logo and designs elements for the updated design. This trade show targets a different customer and the design and copy needs to change. We no longer want the "hub and spoke" graphic in the middle.
Here's the copy...
Headline:
Super Charge Your Email Marketing
Main Copy:
What can email do for you?
• Maximize ROI
• Strengthen relationships
• Drive engagement
• Increase conversions
We handle email—so you can focus on growth.
From a design standpoint I would recommend:
1. Email Iconography:
Use glowing, stylized email icons next to each bullet point to visually break up the text and add a modern, engaging element.
2. Badge for Experience:
Create a prominent badge or ribbon highlighting “Over 20 years of experience,” placed in the bottom corner to emphasize expertise.
3. ROI Graphic:
Incorporate a subtle upward-trending arrow or graph behind the “Maximize ROI” bullet point to visually reinforce the concept of growth and success.
I would like to see a email icon and a lighting bolt somehow incorporated into the main headline of the back drop .
Lastly, the printing specs are attached.
Business Owners

```html
<!DOCTYPE html>
<html lang="en">
<head>
<meta charset="utf-8">
<title>Brightpost Relay – Trade Show Backdrop</title>
<link rel="stylesheet" href="https://fonts.googleapis.com/css2?family=Krona+One&family=Montserrat:wght@500;700;800&family=Bebas+Neue&display=swap">
<style>
  :root {
    --stage: #a4a4a4;
    --white: #ffffff;
    --blush: #fbe6ef;
    --magenta: #ea1f7f;
    --magenta-deep: #d0146b;
    --rose: #e065a4;
    --ink: #1b1b24;
    --photo-dark: #1f2b3d;
    --photo-light: #8995a6;
  }
  * { box-sizing: border-box; margin: 0; padding: 0; }
  html, body { width: 857px; height: 1200px; overflow: hidden; }
  body { background: var(--stage); position: relative; font-family: "Montserrat", sans-serif; }

  .backdrop {
    position: absolute; left: 28px; top: 350px;
    width: 800px; height: 500px;
    background: var(--white);
    overflow: hidden;
    box-shadow: 0 12px 28px rgba(0,0,0,.3);
  }
  .backdrop-shapes { position: absolute; inset: 0; }

  .site-url {
    position: absolute; top: 250px;
    font-family: "Montserrat", sans-serif; font-weight: 700;
    font-size: 14px; color: var(--magenta);
    white-space: nowrap;
    transform-origin: center;
  }
  .site-url.left  { left: 45px;  transform: translate(-50%, -50%) rotate(-90deg); }
  .site-url.right { left: 752px; transform: translate(-50%, -50%) rotate(-90deg); }

  .brand {
    position: absolute; left: 136px; top: 128px;
    display: flex; align-items: center; gap: 10px;
  }
  .brand-square { width: 22px; height: 22px; background: var(--magenta-deep); }
  .brand-name {
    font-family: "Krona One", sans-serif; font-size: 19px;
    color: var(--ink); white-space: nowrap;
  }

  .headline {
    position: absolute; left: 136px; top: 227px;
    font-family: "Krona One", sans-serif; font-size: 20.5px;
    color: var(--ink); white-space: nowrap; letter-spacing: -0.3px;
  }
  .headline .accent { color: var(--magenta); }

  .question-pill {
    position: absolute; left: 135px; top: 264px;
    width: 388px; height: 27px; border-radius: 14px;
    background: var(--rose);
    color: var(--white);
    font-family: "Krona One", sans-serif; font-size: 12px;
    display: flex; align-items: center; justify-content: center;
  }

  .benefits { position: absolute; left: 135px; top: 304px; width: 400px; height: 70px; }
  .benefit {
    position: absolute; display: flex; align-items: center; gap: 9px;
    font-size: 13px; font-weight: 500; color: var(--ink); white-space: nowrap;
  }
  .benefit svg { width: 26px; height: 26px; flex: none; }
  .benefit.roi  { left: 0;     top: 0; }
  .benefit.rel  { left: 181px; top: 0; }
  .benefit.eng  { left: 0;     top: 36px; }
  .benefit.conv { left: 181px; top: 36px; }
  .roi-arrow { position: absolute; left: -20px; top: 2px; width: 14px; height: 16px; }

  .experience-badge { position: absolute; left: 528px; top: 262px; width: 156px; height: 156px; }
  .badge-text {
    position: absolute; inset: 0;
    display: flex; flex-direction: column; align-items: center; justify-content: center;
    font-family: "Bebas Neue", sans-serif; color: var(--white); line-height: .9;
  }
  .badge-text .over  { font-size: 26px; }
  .badge-text .years { font-size: 36px; }
  .badge-text .exp   { font-size: 15px; }

  .tagline {
    position: absolute; left: 0; right: 0; top: 424px;
    text-align: center;
    font-family: "Krona One", sans-serif; font-size: 14.5px;
    color: var(--white); white-space: nowrap;
  }
</style>
</head>
<body>
  <main class="backdrop">
    <svg class="backdrop-shapes" viewBox="0 0 800 500" width="800" height="500">
      <defs>
        <linearGradient id="photoTone" x1="0" y1="0" x2="1" y2="1">
          <stop offset="0" stop-color="var(--photo-dark)"/>
          <stop offset="0.6" stop-color="var(--photo-light)"/>
          <stop offset="1" stop-color="#c9ced8"/>
        </linearGradient>
      </defs>
      <!-- side blush panels -->
      <path class="side-panel" d="M0 0 H115 Q65 130 80 250 Q90 370 140 430 L0 430 Z" fill="var(--blush)"/>
      <path class="side-panel" d="M800 0 H740 Q700 120 705 250 Q710 370 690 430 L800 430 Z" fill="var(--blush)"/>
      <!-- magenta arc framing the photo -->
      <path class="photo-arc" d="M270 0 H760 Q720 200 480 205 Q330 200 270 0 Z" fill="var(--magenta)"/>
      <path d="M290 0 H745 Q700 180 490 190 Q350 185 290 0 Z" fill="var(--white)"/>
      <!-- photo area -->
      <path role="img" aria-label="Photo of hands typing on a laptop with a glowing world network of email icons"
            d="M334 0 H736 Q700 165 490 174 Q380 170 334 0 Z" fill="url(#photoTone)"/>
      <!-- plain circle where the decoration sits -->
      <circle cx="400" cy="150" r="42" fill="var(--white)"/>
      <!-- bottom band -->
      <path class="bottom-band" d="M0 412 Q400 360 800 412 V500 H0 Z" fill="var(--magenta)"/>
    </svg>

    <div class="site-url left">www.brightpostrelay.com</div>
    <div class="site-url right">www.brightpostrelay.com</div>

    <div class="brand">
      <span class="brand-square"></span>
      <span class="brand-name">Brightpost Relay</span>
    </div>

    <h1 class="headline">Super Charge Your <span class="accent">Email Marketing</span></h1>
    <div class="question-pill">What can email do for you?</div>

    <ul class="benefits">
      <svg class="roi-arrow" viewBox="0 0 14 16"><path d="M2 8 L7 3 L12 8 M2 14 L7 9 L12 14" fill="none" stroke="#4fb89a" stroke-width="2"/></svg>
      <li class="benefit roi">
        <svg viewBox="0 0 26 26"><circle cx="13" cy="13" r="13" fill="var(--magenta)"/><path d="M8 19V15M11.5 19V12M15 19V10M18.5 19V7" stroke="#fff" stroke-width="2"/></svg>
        Maximize ROI
      </li>
      <li class="benefit rel">
        <svg viewBox="0 0 26 26"><circle cx="13" cy="13" r="13" fill="var(--magenta)"/><circle cx="13" cy="13" r="4" fill="none" stroke="#fff" stroke-width="1.6"/><circle cx="7" cy="8" r="1.6" fill="#fff"/><circle cx="19" cy="8" r="1.6" fill="#fff"/><circle cx="7" cy="18" r="1.6" fill="#fff"/><circle cx="19" cy="18" r="1.6" fill="#fff"/></svg>
        Strengthen relationships
      </li>
      <li class="benefit eng">
        <svg viewBox="0 0 26 26"><circle cx="13" cy="13" r="13" fill="var(--magenta)"/><rect x="6.5" y="8.5" width="13" height="9" rx="1" fill="none" stroke="#fff" stroke-width="1.6"/><path d="M6.5 9 L13 14 L19.5 9" fill="none" stroke="#fff" stroke-width="1.6"/></svg>
        Drive engagement
      </li>
      <li class="benefit conv">
        <svg viewBox="0 0 26 26"><circle cx="13" cy="13" r="13" fill="var(--magenta)"/><path d="M7 19H19" stroke="#fff" stroke-width="1.6"/><path d="M9 18V14M13 18V11M17 18V8" stroke="#fff" stroke-width="2"/><path d="M15 8 L17 5.5 L19 8" fill="#fff"/></svg>
        Increase conversions
      </li>
    </ul>

    <div class="experience-badge">
      <svg viewBox="0 0 156 156" width="156" height="156">
        <path d="M78 4 Q92 16 104 10 Q112 24 126 24 Q128 40 142 48 Q136 62 148 74 Q138 86 144 102 Q130 108 128 124 Q112 124 104 138 Q90 132 78 146 Q66 132 52 138 Q44 124 28 124 Q26 108 12 102 Q18 86 8 74 Q20 62 14 48 Q28 40 30 24 Q44 24 52 10 Q64 16 78 4 Z" fill="var(--white)" stroke="var(--magenta)" stroke-width="4"/>
        <circle cx="78" cy="76" r="56" fill="var(--rose)"/>
      </svg>
      <div class="badge-text">
        <span class="over">Over</span>
        <span class="years">20 Years</span>
        <span class="exp">Of Experience</span>
      </div>
    </div>

    <p class="tagline">We handle email—so you can focus on growth.</p>
  </main>
</body>
</html>
```